Business Card Design Project

I have just chosen a logo and would now like this designed onto a business card for my hair salon. I would like it to be classy not to busy and have a wow factor when people look at them
Has to Include on card:
Logo Design
And business details below
Kellie-ann Drummond (owner)
0482 736 219
Rdw@vomblet.com.au
71 Willowmere Rise Corvin Cove
Logo is now attached please provide designs
Hair

```html
<!DOCTYPE html>
<html lang="en">
<head>
<meta charset="utf-8">
<title>Corvin Hair Studio – Business Card</title>
<link rel="stylesheet" href="https://fonts.googleapis.com/css2?family=Marcellus&family=Roboto+Condensed:wght@300&display=swap">
<style>
  :root {
    --page-bg: #ece9e6;
    --card-dark: #1c1c1c;
    --damask-light: #4a4a4a;
    --damask-dark: #151515;
    --brand-pink: #e5177e;
    --card-white: #ffffff;
    --panel-purple: #66318f;
    --band-navy: #262366;
    --detail-text: #ffffff;
  }
  * { margin: 0; padding: 0; box-sizing: border-box; }
  html, body {
    width: 1200px;
    height: 1200px;
    overflow: hidden;
    background: var(--page-bg);
  }
  .sheet {
    position: relative;
    width: 1200px;
    height: 1200px;
  }
  .card {
    position: absolute;
    left: 160px;
    width: 880px;
    height: 490px;
    border-radius: 28px;
    overflow: hidden;
    box-shadow: 0 6px 18px rgba(0,0,0,0.18);
  }
  .card--front { top: 80px; background: var(--card-dark); }
  .card--back  { top: 630px; background: var(--card-white); }

  .damask-fill {
    position: absolute;
    inset: 0;
    background: radial-gradient(circle at 50% 50%, var(--damask-light) 0%, #2e2e2e 55%, var(--damask-dark) 100%);
  }

  .brand-name {
    font-family: "Marcellus", serif;
    font-weight: 400;
    color: var(--brand-pink);
    text-transform: uppercase;
    line-height: 1;
  }
  .card--front .brand-name {
    position: absolute;
    left: 0;
    right: 0;
    top: 150px;
    text-align: center;
    font-size: 92px;
    letter-spacing: 2px;
  }
  .card--front .brand-name span { display: block; font-size: 60px; margin-top: 14px; }

  .card--back .brand-name {
    position: absolute;
    left: 8px;
    top: 118px;
    width: 380px;
    text-align: center;
    font-size: 74px;
  }
  .card--back .brand-name span { display: block; font-size: 42px; margin-top: 8px; }

  .back-panel {
    position: absolute;
    inset: 0;
    width: 880px;
    height: 490px;
  }

  .details {
    position: absolute;
    inset: 0;
    font-family: "Roboto Condensed", sans-serif;
    font-weight: 300;
    color: var(--detail-text);
    font-size: 31px;
  }
  .details p { position: absolute; white-space: nowrap; }
  .details .owner   { left: 400px; top: 238px; }
  .details .phone   { left: 385px; top: 283px; letter-spacing: 3px; font-size: 33px; }
  .details .email   { left: 345px; top: 330px; }
  .details .address { left: 312px; top: 375px; letter-spacing: 0.5px; }
</style>
</head>
<body>
<main class="sheet">
  <section class="card card--front">
    <div class="damask-fill" role="img" aria-label="Dark grey damask floral pattern covering the card face"></div>
    <h1 class="brand-name">Corvin <span>Hair Studio</span></h1>
  </section>

  <section class="card card--back">
    <svg class="back-panel" viewBox="0 0 880 490" aria-hidden="true">
      <polygon points="650,0 880,0 880,440 172,440" fill="var(--panel-purple)"/>
      <polygon points="172,440 880,440 880,468 212,468" fill="var(--band-navy)"/>
    </svg>
    <h2 class="brand-name">Corvin <span>Hair Studio</span></h2>
    <div class="details">
      <p class="owner">Kellie-ann Drummond (owner)</p>
      <p class="phone">0482 736 219</p>
      <p class="email">Rdw@vomblet.com.au</p>
      <p class="address">71 Willowmere Rise Corvin Cove</p>
    </div>
  </section>
</main>
</body>
</html>
```